BRELM - Letterhead

Willowmere Institute of Letters and Crafts (BRELM) is a non-profit organization that operates two tuition-free public schools - BRELM Elementary for grades K to 5th and BRELM College Prep for grades 6-12.

We are looking for a letterhead primarily to be used on Google Docs and Microsoft Word. Attached are two versions of our logo. One with our name spelled out and one with the acronym.

For Letterhead, we would like 3 addresses listed:

BRELM HQ
41872 Hollow Brook Lane, Suite 308
Cedar Hollow, CA 90813

BRELM Elementary (K-5)
18460 Marsh Ridge Boulevard
Cedar Hollow, CA 90813

BRELM College Prep (6-12)
27314 Del Sol Terrace
Alder Bay, CA 90817

Our Phone Number is (555) 418-7062
Our Fax Number is the same (555) 418-7062

Our website is www.brelmschools.org

Target Market(s)

Education

Industry/Entity Type

Education

Font styles to use
Sans Serif

Colors
0054AA
0677BA
7BADD7
CADEEF
E8F1F8

Requirements
Must have
• Logo, Address, Phone Number, Website.
Nice to have
• Modern and clean design.
Should not have
• Prefer that there is no bleed -- the letterhead will mostly be used in PDF format however sometimes it will be printed and our printers can not do a full bleed

```html
<!DOCTYPE html>
<html lang="en">
<head>
<meta charset="utf-8">
<title>BRELM Letterhead</title>
<link rel="stylesheet" href="https://fonts.googleapis.com/css2?family=Roboto:wght@400;500;700&display=swap">
<style>
  :root {
    --backdrop: #e9e7e3;
    --paper: #ffffff;
    --brand-navy: #1d3f94;
    --brand-blue: #0054aa;
    --text-blue: #2a63b4;
    --text-muted: #4c7cc0;
    --accent-yellow: #f3c318;
    --accent-orange: #f04e23;
    --accent-green: #2f9e44;
    --accent-sky: #0a7bc6;
    --hex-faint: #f6f7fa;
  }
  * { box-sizing: border-box; margin: 0; padding: 0; }
  html, body {
    width: 1200px;
    height: 800px;
    overflow: hidden;
    background: var(--backdrop);
    font-family: "Roboto", sans-serif;
  }
  .canvas {
    position: relative;
    width: 1200px;
    height: 800px;
  }
  .letterhead {
    position: absolute;
    left: 338px;
    top: 30px;
    width: 523px;
    height: 740px;
    background: var(--paper);
    box-shadow: 0 4px 14px rgba(0,0,0,0.12);
    overflow: hidden;
  }
  .addresses {
    position: absolute;
    left: 31px;
    top: 29px;
    list-style: none;
  }
  .address {
    display: flex;
    align-items: flex-start;
    gap: 5px;
    margin-bottom: 5px;
  }
  .address .pin { width: 7px; height: 9px; margin-top: 1px; flex: none; }
  .address-name {
    display: block;
    font-size: 8px;
    font-weight: 500;
    color: var(--text-blue);
    line-height: 1.2;
  }
  .address-line {
    display: block;
    font-size: 6px;
    color: var(--text-muted);
    line-height: 1.4;
    white-space: nowrap;
  }
  .brand {
    position: absolute;
    right: 33px;
    top: 32px;
    display: flex;
    flex-direction: column;
    align-items: center;
    gap: 6px;
  }
  .brand-square {
    width: 54px;
    height: 54px;
    background: var(--brand-blue);
  }
  .brand-name {
    font-size: 21px;
    font-weight: 500;
    color: var(--brand-navy);
    letter-spacing: 0.5px;
    line-height: 1;
  }
  .faint-pattern {
    position: absolute;
    left: 315px;
    top: 127px;
    width: 208px;
    height: 387px;
    background: linear-gradient(160deg, rgba(246,247,250,0) 0%, var(--hex-faint) 45%, rgba(246,247,250,0) 100%);
  }
  .corner-accent {
    position: absolute;
    left: 0;
    bottom: 0;
    width: 137px;
    height: 89px;
    background: linear-gradient(90deg, var(--accent-yellow) 0%, var(--accent-orange) 40%, var(--accent-sky) 70%, var(--brand-navy) 100%);
  }
  .contact {
    position: absolute;
    right: 31px;
    bottom: 17px;
    display: flex;
    align-items: center;
    gap: 8px;
    font-size: 8px;
    color: var(--text-blue);
  }
  .contact-item { display: flex; align-items: center; gap: 3px; }
  .contact-item svg { width: 7px; height: 7px; }
</style>
</head>
<body>
<main class="canvas">
  <article class="letterhead">
    <ul class="addresses">
      <li class="address">
        <svg class="pin" viewBox="0 0 10 13"><path d="M5 0a5 5 0 0 0-5 5c0 3.6 5 8 5 8s5-4.4 5-8a5 5 0 0 0-5-5zm0 7a2 2 0 1 1 0-4 2 2 0 0 1 0 4z" fill="var(--text-blue)"/></svg>
        <div>
          <span class="address-name">BRELM HQ</span>
          <span class="address-line">41872 Hollow Brook Lane, Suite 308 Cedar Hollow, CA 90813</span>
        </div>
      </li>
      <li class="address">
        <svg class="pin" viewBox="0 0 10 13"><path d="M5 0a5 5 0 0 0-5 5c0 3.6 5 8 5 8s5-4.4 5-8a5 5 0 0 0-5-5zm0 7a2 2 0 1 1 0-4 2 2 0 0 1 0 4z" fill="var(--text-blue)"/></svg>
        <div>
          <span class="address-name">BRELM College Prep (6-12)</span>
          <span class="address-line">27314 Del Sol Terrace Alder Bay, CA 90817</span>
        </div>
      </li>
      <li class="address">
        <svg class="pin" viewBox="0 0 10 13"><path d="M5 0a5 5 0 0 0-5 5c0 3.6 5 8 5 8s5-4.4 5-8a5 5 0 0 0-5-5zm0 7a2 2 0 1 1 0-4 2 2 0 0 1 0 4z" fill="var(--text-blue)"/></svg>
        <div>
          <span class="address-name">BRELM Elementary (K-5)</span>
          <span class="address-line">18460 Marsh Ridge Boulevard Cedar Hollow, CA 90813</span>
        </div>
      </li>
    </ul>

    <div class="brand">
      <div class="brand-square"></div>
      <span class="brand-name">BRELM</span>
    </div>

    <div class="faint-pattern" role="img" aria-label="Faint background pattern"></div>

    <div class="corner-accent" role="img" aria-label="Brand colour accent in the lower corner"></div>

    <div class="contact">
      <span class="contact-item">
        <svg viewBox="0 0 10 10"><path d="M2 0.5l1.6 2.2-1 1.2a6 6 0 0 0 3.5 3.5l1.2-1 2.2 1.6-0.8 1.6C5 9.6 0.4 5 0.4 1.3z" fill="var(--text-blue)"/></svg>
        (555) 418-7062
      </span>
      <span class="contact-item">
        <svg viewBox="0 0 10 10"><circle cx="5" cy="5" r="4.2" fill="none" stroke="var(--text-blue)" stroke-width="1.2"/><path d="M1 5h8M5 1c-2 2.4-2 5.6 0 8M5 1c2 2.4 2 5.6 0 8" fill="none" stroke="var(--text-blue)" stroke-width="0.8"/></svg>
        www.brelmschools.org
      </span>
    </div>
  </article>
</main>
</body>
</html>
```